New Website for Consulting Company

Our company needs a fresh web design to help us drive our business forward. We are a consulting and software provider to Airports, Air Traffic Organizations, Builders and Architects. We specialize in analyzing operations, monitoring noise levels and creating software to improve operations, meet customer requirements and improve public relations.
Additional Info:
- Additional requirements can be found in the Web Design Brief
- Logo and logo branding attached
Target Market(s)
Airlines, Airports, Government Agencies, and Real Estate Developers
Industry/Entity Type
Aviation
Coding
Coded - Design and coding required
Number of Pages Required
2 page
Colors
Designer to choose colors to be used in the design.
Requirements
Must have
- - Create a Wordpress Design (Coded - Design and coding required)
- - Designer must provide full implementation/coding depending on the platform chosen by the client (i.e. Wordpress theme, HTML/CSS, etc.)
- - This is a multi-page site; Supporting pages can be formatted the same, but links need to be in place
- - Colors used must be grey scale, black or match the logo. It is not necessary to use all the colors in our logo
Should not have
- We are not looking for an overly bright site. While our logo has 5 different colors, it is not necessary to use all of them.

```html
<!DOCTYPE html>
<html lang="en">
<head>
<meta charset="utf-8">
<title>SkyMeridian International</title>
<link href="https://fonts.googleapis.com/css2?family=Roboto:wght@300;400;500;700;900&display=swap" rel="stylesheet">
<style>
:root{
  --blue:#2b78b5;
  --ink:#1e1e1e;
  --text:#555;
  --muted:#9a9a9a;
  --panel:#ececec;
  --dark:#262626;
  --darker:#2b2b2b;
  --white:#fff;
  --line:#bdbdbd;
}
*{margin:0;padding:0;box-sizing:border-box}
html,body{width:1200px;height:2490px;overflow:hidden}
body{position:relative;background:var(--white);font-family:'Roboto',sans-serif;color:var(--ink)}
a{color:inherit;text-decoration:none}

/* header */
.site-header{position:absolute;left:0;top:0;width:1200px;height:62px;background:linear-gradient(#fafafa,#ececec);border-top:3px solid #555}
.brand{position:absolute;left:161px;top:16px;display:flex;align-items:center;gap:8px;font-size:24px;font-weight:700;color:var(--ink)}
.brand-dot{width:14px;height:14px;background:var(--blue);border-radius:50%}
.main-nav{position:absolute;right:161px;top:24px;display:flex;gap:20px;font-size:12px;font-weight:500;color:#222}

/* hero */
.hero{position:absolute;left:0;top:62px;width:1200px;height:476px;background:linear-gradient(180deg,#7d92a3 0%,#c9b58e 45%,#a58a62 60%,#6b5a47 100%)}
.hero-tagline{position:absolute;right:162px;bottom:50px;font-size:20px;font-weight:500;color:rgba(255,255,255,.85);letter-spacing:.3px}

/* welcome */
.welcome-media{position:absolute;left:161px;top:621px;width:405px;height:317px;background:linear-gradient(180deg,#6fb6e8 0%,#a9d6f2 55%,#5fa63a 75%,#3f7d2a 100%)}
.welcome-panel{position:absolute;left:566px;top:589px;width:472px;height:379px;background:var(--panel);padding:22px 26px 0 28px}
.welcome-kicker{font-size:26px;font-weight:300;color:#222;line-height:1}
.welcome-title{font-size:29px;font-weight:500;color:var(--blue);margin:2px 0 12px 22px;line-height:1.15;white-space:nowrap}
.welcome-panel p{font-size:10.6px;line-height:1.5;color:var(--text);margin-bottom:10px;padding-left:3px}
.btn-more{position:absolute;left:31px;bottom:22px;display:inline-flex;align-items:center;gap:5px;height:32px;padding:0 16px;border:2px solid #333;font-size:10px;font-weight:700;color:#222}

/* services */
.services{position:absolute;left:0;top:1019px;width:1200px;height:337px;background:var(--dark)}
.service{position:absolute;top:38px;width:209px;height:263px;border:3px solid #8a8a8a;text-align:center;padding-top:32px}
.service-icon{width:82px;height:82px;margin:0 auto;border-radius:50%;background:#bdbdbd;display:flex;align-items:center;justify-content:center}
.service h3{font-size:21px;font-weight:400;color:#e6e6e6;margin:22px 0 12px}
.service p{font-size:11px;line-height:1.55;color:#6a6a6a;padding:0 20px}

/* videos */
.videos{position:absolute;left:0;top:1356px;width:1200px;height:360px;background:linear-gradient(180deg,#c99a47 0%,#e0aa48 45%,#c0812f 75%,#2a2219 100%);overflow:hidden}
.videos h2{position:absolute;left:0;right:0;top:110px;text-align:center;font-size:46px;font-weight:900;color:var(--white);letter-spacing:-.5px}
.video-play{position:absolute;left:545px;top:182px}
.award-ribbon{position:absolute;right:-60px;bottom:30px;width:260px;height:46px;background:#4f8f2a;transform:rotate(-45deg);border:2px solid #d8d02a}

/* news */
.news-head{position:absolute;left:0;top:1752px;width:1200px;text-align:center}
.news-head h2{font-size:30px;font-weight:700;color:#222}
.news-head p{font-size:11px;color:var(--muted);margin-top:12px}
.news-divider{position:absolute;left:315px;top:1824px;width:570px;height:16px}
.news-card{position:absolute;top:1877px;width:272px}
.news-photo{height:200px}
.news-meta{position:relative;margin-top:18px;padding-left:55px;min-height:120px}
.news-date{position:absolute;left:0;top:0;width:38px;height:38px;background:#2a2a2a;color:var(--white);text-align:center;font-size:11px;font-weight:700;line-height:1.25;padding-top:4px}
.news-meta h3{font-size:14px;font-weight:700;color:#222;padding-top:8px}
.news-meta p{font-size:11px;line-height:1.55;color:var(--text);margin-top:10px}
.news-actions{position:absolute;left:0;top:366px;width:272px;height:35px;background:var(--blue);display:flex;justify-content:space-between;align-items:center;padding:0 16px 0 14px;font-size:11px;color:var(--white)}
.news-actions span{display:flex;align-items:center;gap:5px}

/* footer */
.site-footer{position:absolute;left:0;top:2345px;width:1200px;height:145px;background:var(--darker);text-align:center;color:#ddd}
.footer-nav{margin-top:36px;font-size:13px;display:flex;justify-content:center;gap:18px}
.footer-nav .sep{color:#aaa}
.copyright{font-size:10px;color:#aaa;margin-top:12px}
.social{display:flex;justify-content:center;gap:14px;margin-top:16px}
.social span{width:24px;height:24px;border:1.5px solid #ccc;border-radius:50%}
</style>
</head>
<body>

<header class="site-header">
  <a class="brand" href="#"><span class="brand-dot"></span>SkyMeridian</a>
  <nav class="main-nav">
    <a href="#">HOME</a><a href="#">AIRPORTS</a><a href="#">AIRSPACE</a><a href="#">EMISSIONS</a><a href="#">ACOUSTICS</a><a href="#">VISUALIZATION</a><a href="#">CONTACT</a>
  </nav>
</header>

<section class="hero" role="img" aria-label="Front view of a passenger jet on the apron at sunrise">
  <div class="hero-tagline">AVIATION.TECHNOLGY. VISUALIZED.</div>
</section>

<section class="welcome">
  <div class="welcome-media" role="img" aria-label="Illustration of a plane flying over a city skyline with flight data labels and a green runway"></div>
  <div class="welcome-panel">
    <div class="welcome-kicker">WELCOME TO</div>
    <h1 class="welcome-title">SkyMeridian International</h1>
    <p>Lorem Ipsum is simply dummy text of the printing and typesetting industry. Lorem Ipsum printer took a galley of type and scrambled it to make a type specimen book. It has survived not only five centuries, but also the leap into electronic typesetting, remaining essentially unchanged. It was popularised in the 1960s with the release of Typeleaf sheets containing Lorem Ipsum passages, and more recently with desktop publishing software like Quillset Composer including versions of Lorem Ipsum.</p>
    <p>Lorem Ipsum is simply dummy text of the printing and typesetting industry. Lorem Ipsum printer took a galley of type and scrambled it to make a type specimen book. It has survived not only five centuries, but also the leap into electronic typesetting, remaining essentially Lorem Ipsum passages, and more recently with desktop publishing software like Quillset Composer including versions of Lorem Ipsum.</p>
    <a class="btn-more" href="#">READ MORE
      <svg width="10" height="10" viewBox="0 0 10 10"><circle cx="5" cy="5" r="5" fill="#222"/><path d="M4 2.5 6.5 5 4 7.5" stroke="#fff" stroke-width="1.4" fill="none"/></svg>
    </a>
  </div>
</section>

<section class="services">
  <div class="service" style="left:163px">
    <div class="service-icon">
      <svg width="44" height="44" viewBox="0 0 24 24"><path fill="#2a2a2a" d="M21 16v-2l-8-5V3.5a1.5 1.5 0 0 0-3 0V9l-8 5v2l8-2.5V19l-2 1.5V22l3.5-1 3.5 1v-1.5L13 19v-5.5z" transform="rotate(45 12 12)"/></svg>
    </div>
    <h3>Airports</h3>
    <p>the printing and typesetting industry. into electronic typesetting, remaining Lorem Ipsum.</p>
  </div>
  <div class="service" style="left:384px">
    <div class="service-icon">
      <svg width="46" height="46" viewBox="0 0 24 24" fill="none" stroke="#2a2a2a" stroke-width="1.6"><path d="M12 3 20 7.5v9L12 21l-8-4.5v-9z"/><path d="M4 7.5 12 12l8-4.5M12 12v9"/><circle cx="12" cy="7.5" r="1.5"/></svg>
    </div>
    <h3>Software</h3>
    <p>the printing and typesetting industry. into electronic typesetting, remaining Lorem Ipsum.</p>
  </div>
  <div class="service" style="left:606px">
    <div class="service-icon">
      <svg width="46" height="46" viewBox="0 0 24 24" fill="none" stroke="#2a2a2a" stroke-width="1.6"><path d="M4 9h4l5-4v14l-5-4H4z"/><path d="M16 9a4 4 0 0 1 0 6M18.5 6.5a7.5 7.5 0 0 1 0 11"/></svg>
    </div>
    <h3>Noise &amp; Emissions</h3>
    <p>the printing and typesetting industry. into electronic typesetting, remaining Lorem Ipsum.</p>
  </div>
  <div class="service" style="left:827px">
    <div class="service-icon">
      <svg width="46" height="46" viewBox="0 0 24 24" fill="none" stroke="#2a2a2a" stroke-width="1.5"><circle cx="12" cy="12" r="2.5"/><circle cx="5" cy="5" r="2"/><circle cx="19" cy="5" r="2"/><circle cx="5" cy="19" r="2"/><circle cx="19" cy="19" r="2"/><circle cx="12" cy="3" r="1.5"/><path d="M6.5 6.5 10 10M17.5 6.5 14 10M6.5 17.5 10 14M17.5 17.5 14 14M12 4.5v5"/></svg>
    </div>
    <h3>Visualization</h3>
    <p>the printing and typesetting industry. into electronic typesetting, remaining Lorem Ipsum.</p>
  </div>
</section>

<section class="videos" role="img" aria-label="Passenger jet landing over a runway against an orange sunset sky">
  <h2>OUR VIDEOS</h2>
  <svg class="video-play" width="70" height="52" viewBox="0 0 70 52" fill="none" stroke="#fff" stroke-width="2.5">
    <rect x="2" y="2" width="66" height="48"/>
    <path d="M2 10h66M2 42h66M12 2v8M22 2v8M32 2v8M42 2v8M52 2v8M62 2v8M12 42v8M22 42v8M32 42v8M42 42v8M52 42v8M62 42v8"/>
    <path d="M29 18v16l12-8z"/>
  </svg>
  <div class="award-ribbon"></div>
</section>

<section class="news">
  <div class="news-head">
    <h2>LATEST NEWS</h2>
    <p>Lorem Ipsum is simply dummy text of the printing and typesetting industry.</p>
  </div>
  <svg class="news-divider" viewBox="0 0 570 16">
    <rect x="0" y="6" width="570" height="4" fill="#e3e3e3"/>
    <rect x="245" y="0" width="80" height="16" fill="#fff"/>
    <path fill="#333" d="M262 3l1.8 3.6 4 .6-2.9 2.8.7 4-3.6-1.9-3.6 1.9.7-4-2.9-2.8 4-.6z"/>
    <path fill="var(--blue)" d="M285 1l2.4 4.8 5.3.8-3.8 3.7.9 5.3-4.8-2.5-4.8 2.5.9-5.3-3.8-3.7 5.3-.8z"/>
    <path fill="#333" d="M308 3l1.8 3.6 4 .6-2.9 2.8.7 4-3.6-1.9-3.6 1.9.7-4-2.9-2.8 4-.6z"/>
  </svg>

  <article class="news-card" style="left:161px">
    <div class="news-photo" role="img" aria-label="Airliner taking off into a bright hazy sky" style="background:linear-gradient(180deg,#9fb0bd,#e8dcc4 55%,#b8a68a)"></div>
    <div class="news-meta">
      <div class="news-date">15<br>DEC</div>
      <h3>Lorem Ipsum is simply dummy</h3>
      <p>Lorem Ipsum is simply dummy text of the centuries, but also the leap into electronic typesetting, remaining essentially release Typeleaf Composer including versions text Lorem Ipsum.</p>
    </div>
    <div class="news-actions">
      <span><svg width="12" height="11" viewBox="0 0 12 11"><path fill="#fff" d="M6 0C2.7 0 0 2 0 4.6c0 1.4.8 2.6 2 3.4L1.5 11 4.4 9c.5.1 1 .2 1.6.2 3.3 0 6-2 6-4.6S9.3 0 6 0z"/></svg>Comments</span>
      <span><svg width="12" height="11" viewBox="0 0 12 11"><path fill="#fff" d="M6 11 1 6A3 3 0 0 1 6 1.8 3 3 0 0 1 11 6z"/></svg>0 Likes</span>
      <span><svg width="11" height="11" viewBox="0 0 11 11" fill="#fff" stroke="#fff"><circle cx="9" cy="2" r="1.6"/><circle cx="2" cy="5.5" r="1.6"/><circle cx="9" cy="9" r="1.6"/><path d="M9 2 2 5.5 9 9" fill="none"/></svg>Share</span>
    </div>
  </article>

  <article class="news-card" style="left:466px">
    <div class="news-photo" role="img" aria-label="Businessman in a suit using a phone with floating app tiles" style="background:linear-gradient(180deg,#e6e6e6,#b5b5b5 60%,#3a3a3a)"></div>
    <div class="news-meta">
      <div class="news-date">15<br>DEC</div>
      <h3>Lorem Ipsum is simply dummy</h3>
      <p>Lorem Ipsum is simply dummy text of the centuries, but also the leap into electronic typesetting, remaining essentially release Typeleaf Composer including versions text Lorem Ipsum.</p>
    </div>
    <div class="news-actions">
      <span><svg width="12" height="11" viewBox="0 0 12 11"><path fill="#fff" d="M6 0C2.7 0 0 2 0 4.6c0 1.4.8 2.6 2 3.4L1.5 11 4.4 9c.5.1 1 .2 1.6.2 3.3 0 6-2 6-4.6S9.3 0 6 0z"/></svg>Comments</span>
      <span><svg width="12" height="11" viewBox="0 0 12 11"><path fill="#fff" d="M6 11 1 6A3 3 0 0 1 6 1.8 3 3 0 0 1 11 6z"/></svg>0 Likes</span>
      <span><svg width="11" height="11" viewBox="0 0 11 11" fill="#fff" stroke="#fff"><circle cx="9" cy="2" r="1.6"/><circle cx="2" cy="5.5" r="1.6"/><circle cx="9" cy="9" r="1.6"/><path d="M9 2 2 5.5 9 9" fill="none"/></svg>Share</span>
    </div>
  </article>

  <article class="news-card" style="left:767px">
    <div class="news-photo" role="img" aria-label="Passenger jet on a runway at sunset" style="background:linear-gradient(180deg,#6f8aa8,#e3c48a 55%,#8a7150)"></div>
    <div class="news-meta">
      <div class="news-date">15<br>DEC</div>
      <h3>Lorem Ipsum is simply dummy</h3>
      <p>Lorem Ipsum is simply dummy text of the centuries, but also the leap into electronic typesetting, remaining essentially release Typeleaf Composer including versions text Lorem Ipsum.</p>
    </div>
    <div class="news-actions">
      <span><svg width="12" height="11" viewBox="0 0 12 11"><path fill="#fff" d="M6 0C2.7 0 0 2 0 4.6c0 1.4.8 2.6 2 3.4L1.5 11 4.4 9c.5.1 1 .2 1.6.2 3.3 0 6-2 6-4.6S9.3 0 6 0z"/></svg>Comments</span>
      <span><svg width="12" height="11" viewBox="0 0 12 11"><path fill="#fff" d="M6 11 1 6A3 3 0 0 1 6 1.8 3 3 0 0 1 11 6z"/></svg>0 Likes</span>
      <span><svg width="11" height="11" viewBox="0 0 11 11" fill="#fff" stroke="#fff"><circle cx="9" cy="2" r="1.6"/><circle cx="2" cy="5.5" r="1.6"/><circle cx="9" cy="9" r="1.6"/><path d="M9 2 2 5.5 9 9" fill="none"/></svg>Share</span>
    </div>
  </article>
</section>

<footer class="site-footer">
  <nav class="footer-nav">
    <a href="#">Home</a><span class="sep">|</span><a href="#">Airports</a><span class="sep">|</span><a href="#">Airspace</a><span class="sep">|</span><a href="#">Emissions</a><span class="sep">|</span><a href="#">Acoustics</a><span class="sep">|</span><a href="#">Visualization</a><span class="sep">|</span><a href="#">Contact</a>
  </nav>
  <div class="copyright">© 2017 skyMeridianInternational . All rights reserved</div>
  <div class="social"><span></span><span></span></div>
</footer>

</body>
</html>
```